Cover Art Design for a Notebook

We are going to give away some note books to our marketing department and want an elegant art design for the cover. There is a theme centered around ABCD of marketing that we want to leverage in the design. So these letters should be prominent in the design. The ABCD stand for Agility, Boost, Customer, Data.

If you could Cleverly incorporate these words into the letters with a good design that would be good.

But please make the ABCD the focus of the artwork. The words associated with them should be subtle, in the background, visible but not the focus.

We are looking for stylish. We want people to feel proud of the ELEGANT DESIGN when they take out this notebook for business.

Also worth mentioning- We are a biotechnology company so if you incorporate elements in that theme in, on, or around the ABCD letters, it could be a good idea. As long as it doesn’t kill the rest of the design.

I will upload our logo for Veltrane Orwick Biologics later (you can see it online) and this will need to go in one corner.

Notebook will be A5 format. Image on front cover only. Need ASAP.

(Do not make baby blocks as we don’t want something that looks like a kids book)

Target Market(s)

business people who feel proud to pull out this notebook

Industry/Entity Type

Biotechnology

Colors
ec1f27
ffffff
000000

Requirements
Must have
• ELEGANT ART DESIGN USING ABCD
Nice to have
• see brief above
Should not have
• baby blocks

```html
<!DOCTYPE html>
<html lang="en">
<head>
<meta charset="utf-8">
<title>ABCD of Marketing — Notebook Cover</title>
<link rel="stylesheet" href="https://fonts.googleapis.com/css2?family=Great+Vibes&family=Open+Sans:wght@400&display=swap">
<style>
  :root {
    --brand-red: #ec1f27;
    --ink-black: #000000;
    --paper-white: #ffffff;
    --pattern-grey: #f1f1f1;
    --logo-grey: #1a1a1a;
  }
  html, body {
    margin: 0;
    padding: 0;
    overflow: hidden;
    background: var(--paper-white);
  }
  .cover {
    position: relative;
    width: 847px;
    height: 1200px;
    overflow: hidden;
    background: linear-gradient(180deg, var(--pattern-grey) 0%, #f7f7f7 50%, var(--pattern-grey) 100%);
  }
  .background-texture {
    position: absolute;
    inset: 0;
    width: 100%;
    height: 100%;
  }
  .logo-slot {
    position: absolute;
    top: 36px;
    right: 46px;
    margin: 0;
    font-family: "Open Sans", sans-serif;
    font-size: 33px;
    font-weight: 400;
    color: var(--logo-grey);
  }
  .flourishes {
    position: absolute;
    inset: 0;
    width: 100%;
    height: 100%;
  }
  .initial,
  .keyword {
    position: absolute;
    margin: 0;
    font-family: "Great Vibes", cursive;
    font-weight: 400;
    line-height: 1;
    white-space: nowrap;
  }
  .initial {
    color: var(--brand-red);
    font-size: 190px;
  }
  .keyword {
    color: var(--ink-black);
    font-size: 66px;
  }
  .initial--a { left: 70px;  top: 300px; }
  .keyword--agility { left: 262px; top: 345px; }
  .initial--b { left: 150px; top: 440px; }
  .keyword--boost { left: 66px;  top: 490px; }
  .initial--c { left: 395px; top: 590px; }
  .keyword--customer { left: 528px; top: 650px; }
  .initial--d { left: 150px; top: 860px; }
  .keyword--data { left: 358px; top: 935px; }
</style>
</head>
<body>
  <main class="cover">
    <svg class="background-texture" viewBox="0 0 847 1200" role="img" aria-label="Subtle light grey wave-and-dot background pattern">
      <rect width="847" height="1200" fill="var(--pattern-grey)"/>
    </svg>

    <p class="logo-slot">your logo here</p>

    <svg class="flourishes" viewBox="0 0 847 1200" role="img" aria-label="Red calligraphic swash flourishes looping around the initials A, B, C and D">
      <defs>
        <radialGradient id="swash-tint" cx="50%" cy="50%" r="50%">
          <stop offset="0%" stop-color="#ec1f27" stop-opacity="0.16"/>
          <stop offset="100%" stop-color="#ec1f27" stop-opacity="0"/>
        </radialGradient>
      </defs>
      <ellipse cx="250" cy="275" rx="150" ry="95" fill="url(#swash-tint)"/>
      <ellipse cx="360" cy="665" rx="155" ry="70" fill="url(#swash-tint)"/>
      <ellipse cx="645" cy="535" rx="150" ry="80" fill="url(#swash-tint)"/>
      <ellipse cx="330" cy="850" rx="165" ry="60" fill="url(#swash-tint)"/>
    </svg>

    <h1 class="initial initial--a">A</h1>
    <span class="keyword keyword--agility">agility</span>

    <h1 class="initial initial--b">B</h1>
    <span class="keyword keyword--boost">boost</span>

    <h1 class="initial initial--c">C</h1>
    <span class="keyword keyword--customer">customer</span>

    <h1 class="initial initial--d">D</h1>
    <span class="keyword keyword--data">data</span>
  </main>
</body>
</html>
```